Wine label for boutique family-owned winery

We need a front wine label designed for Velmora, our small, family-owned, Oregon based winery . Velmora makes warm climate red blends with grapes sourced from SE Washington state, USA. We are a startup business with wines for 2013 and 2014.

The name Velmora comes from the Georgian language, and is short for Tobias, my father's name. The Georgians have an 5000-8000 year history of winemaking, out of which they give heartfelt toasts that celebrate kinship, family, and loved ones of the past and future.

The design can be of various aspect ratios, but should fit flatly on a bordeaux style wine bottle.
We would like this wine label to work for red wines, and be convertible to work with white wines with some simple background color changes. The preferred file format is Adobe Illustrator. This label will be digitally printed.

A couple wine labels that I like:
- 9 Lanterns
- brelvastudio.com/labels "amber"

I am including a file to show what the existing Velmora label looks like.
Updates

Project Deadline Extended
Reason: To give more time for designer revisions. We want the right design!

Target Market(s)

Direct sales through group tastings.
Professionals aged 30-65 with disposable income.
$35/bottle wine.

Industry/Entity Type

Boutique

Font styles to use
Serif
Decorative
Script

Requirements
Must have
• Rich and/or earthy tones (see link to "Amber" above)
• The text on the front label will include:
• The brand name- Velmora
• Vintage: 2013
• Wine name- Corvalé Blend
• AVA: Washington State
• (The specific information will vary, but we need room for those categories of text.)
Nice to have
• We'd like to convey the qualities of sincerity, trustworthiness, and being grounded. If it's possible to convey our philosophy of sharing wine with friends and family that would be great.
• We have an existing logo "Velmora" that has been attached as an SVG file.
• It is not required to include this logo, but if it works in your design, all the better.
Should not have
• Feature photographs or likenesses of photographs

```html
<!DOCTYPE html>
<html lang="en">
<head>
<meta charset="utf-8">
<title>Velmora – Front Wine Label</title>
<link rel="stylesheet" href="https://fonts.googleapis.com/css2?family=Saira+Extra+Condensed:wght@500;600&family=Saira+Condensed:wght@500&display=swap">
<style>
  :root {
    --backdrop: #e9731f;
    --label-light: #ffb43e;
    --label-mid: #f9a32c;
    --label-edge: #f39324;
    --ink-purple: #4a2366;
    --scene-sky: #f2a03a;
    --scene-trees: #4e2465;
    --scene-field: #8a4a6a;
    --scene-water: #e3883a;
  }
  * { margin: 0; padding: 0; box-sizing: border-box; }
  html, body {
    width: 1200px;
    height: 2699px;
    overflow: hidden;
    background: var(--backdrop);
  }
  .canvas {
    position: relative;
    width: 1200px;
    height: 2699px;
  }
  .label {
    position: absolute;
    left: 100px;
    top: 824px;
    width: 1000px;
    height: 1050px;
    overflow: hidden;
    background: linear-gradient(180deg, var(--label-edge) 0%, var(--label-light) 22%, var(--label-mid) 60%, var(--label-edge) 100%);
    color: var(--ink-purple);
  }
  .label-heading {
    position: absolute;
    top: 0;
    left: 0;
    width: 1000px;
    height: 500px;
  }
  .brand-name {
    font-family: "Saira Extra Condensed", "Arial Narrow", sans-serif;
    font-weight: 600;
    font-size: 330px;
    fill: var(--ink-purple);
  }
  .wine-details {
    font-family: "Saira Condensed", "Arial Narrow", sans-serif;
    font-weight: 500;
    font-size: 30px;
    fill: var(--ink-purple);
  }
  .landscape {
    position: absolute;
    top: 590px;
    left: 0;
    width: 100%;
    height: 310px;
    background: linear-gradient(180deg,
      var(--scene-sky) 0%,
      var(--scene-trees) 14%,
      var(--scene-trees) 26%,
      var(--scene-field) 40%,
      var(--scene-field) 72%,
      var(--scene-water) 82%,
      var(--scene-field) 100%);
    opacity: 0.92;
  }
  .bottle-specs {
    position: absolute;
    top: 950px;
    right: 96px;
    display: flex;
    gap: 56px;
    white-space: nowrap;
    font-family: "Saira Condensed", "Arial Narrow", sans-serif;
    font-weight: 500;
    font-size: 32px;
    letter-spacing: 3px;
  }
</style>
</head>
<body>
  <main class="canvas">
    <section class="label">
      <svg class="label-heading" viewBox="0 0 1000 500" aria-labelledby="brand-title">
        <text id="brand-title" class="brand-name" x="60" y="390" textLength="880" lengthAdjust="spacingAndGlyphs">VELMORA</text>
        <text class="wine-details" x="60" y="456" textLength="880" lengthAdjust="spacing">2013  -  CORVALÉ BLEND  -  WASHINGTON STATE</text>
      </svg>
      <div class="landscape" role="img" aria-label="Purple-toned landscape of a tree line over an open field reflected in still water, with a lone figure standing in the middle"></div>
      <p class="bottle-specs"><span>17% VOL</span><span>250ML</span></p>
    </section>
  </main>
</body>
</html>
```